Medical VIP club - small design

Please read the specs in a design brief attached. Also we don't have logo in a Vector format and attaching the only version we have.

Industry/Entity Type

Club

```html
<!DOCTYPE html>
<html lang="en">
<head>
<meta charset="utf-8">
<title>Vitalis – Services</title>
<link href="https://fonts.googleapis.com/css2?family=Arimo:wght@400;700&display=swap" rel="stylesheet">
<style>
  :root {
    --page-dark: #1b3675;
    --page-band: #b9cdf2;
    --brand-blue: #1769d6;
    --brand-deep: #0a3fa8;
    --tab-top: #3a8ff0;
    --tab-bottom: #0b55d4;
    --tab-active-top: #5cc0f7;
    --tab-active-bottom: #1c8ae6;
    --tab-reg-top: #2a4fe0;
    --tab-reg-bottom: #0a1fb8;
    --panel-bg: #ffffff;
    --table-head-top: #6e6fb8;
    --table-head-bottom: #3e3f91;
    --table-line: #c9c9cf;
    --text-body: #333333;
    --text-white: #ffffff;
    --phone-text: #1a2a8a;
  }
  * { box-sizing: border-box; margin: 0; padding: 0; }
  html, body { width: 1200px; height: 876px; overflow: hidden; }
  body {
    position: relative;
    font-family: "Arimo", Arial, sans-serif;
    background: linear-gradient(180deg, #3a4f86 0px, var(--page-dark) 60px, var(--page-dark) 236px, var(--page-band) 240px, #e8f0fc 262px, var(--page-dark) 279px, var(--page-dark) 876px);
  }
  .site-header {
    position: absolute; left: 24px; top: 10px; width: 1158px; height: 188px;
    border-radius: 14px; overflow: hidden;
    background: linear-gradient(90deg, #ffffff 0%, #ffffff 28%, #c4d4ee 55%, #9fb6dc 60%);
    border: 2px solid #ffffff;
  }
  .brand {
    position: absolute; left: 40px; top: 72px;
    display: flex; align-items: center; gap: 12px;
    color: var(--brand-blue); font-size: 52px; font-weight: 700; letter-spacing: -1px;
  }
  .brand-mark { width: 34px; height: 34px; border-radius: 50%; background: var(--brand-blue); }
  .header-photo {
    position: absolute; left: 620px; top: 0; width: 540px; height: 188px;
    background: linear-gradient(180deg, #8fb3d9 0%, #c9dbe9 45%, #b8a996 75%, #8a7563 100%);
  }
  .header-photo::before {
    content: ""; position: absolute; left: 0; top: 0; width: 90px; height: 100%;
    background: linear-gradient(90deg, #a9bde0, rgba(169,189,224,0));
  }
  .phone-icon { position: absolute; left: 762px; top: 51px; }
  .phone-number {
    position: absolute; left: 916px; top: 80px;
    font-size: 44px; font-weight: 700; color: var(--phone-text);
    letter-spacing: -1px;
    text-shadow: 0 0 3px #ffffff, 0 0 3px #ffffff;
  }
  .main-nav {
    position: absolute; left: 24px; top: 206px; display: flex; gap: 2px;
  }
  .nav-tab {
    width: 191px; height: 73px; border-radius: 12px 12px 0 0;
    background: linear-gradient(180deg, var(--tab-top) 0%, #2a79ea 50%, var(--tab-bottom) 52%, #1767e0 100%);
    color: var(--text-white); font-size: 20px;
    display: flex; align-items: center; justify-content: center;
    border: 1px solid #6aa8f4; border-bottom: none;
  }
  .nav-tab.is-active { background: linear-gradient(180deg, var(--tab-active-top) 0%, #3aa6ee 50%, var(--tab-active-bottom) 52%, #2496ea 100%); }
  .nav-tab.is-register { background: linear-gradient(180deg, var(--tab-reg-top) 0%, #1d3ad0 50%, var(--tab-reg-bottom) 52%, #1227c4 100%); }
  .content-panel {
    position: absolute; left: 18px; top: 289px; width: 1170px; height: 485px;
    background: var(--panel-bg); border-radius: 14px; overflow: hidden;
    border: 1px solid #9fb4dc;
  }
  .panel-title {
    height: 54px; padding-left: 26px; display: flex; align-items: center;
    background: linear-gradient(180deg, #2b78ea 0%, #1462d8 55%, var(--brand-deep) 100%);
    color: var(--text-white); font-size: 24px;
  }
  .packages {
    position: absolute; left: 25px; top: 81px; width: 1110px;
    border-collapse: collapse; font-size: 14px; color: var(--text-body);
  }
  .packages th {
    height: 35px; font-size: 15px; font-weight: 700; color: var(--text-white);
    background: linear-gradient(180deg, var(--table-head-top), var(--table-head-bottom));
    border-right: 1px solid #c9c9e6;
  }
  .packages th:last-child { border-right: none; }
  .packages td {
    height: 35.3px; border: 1px solid var(--table-line); padding-left: 24px;
  }
  .packages td:nth-child(2), .packages td:nth-child(3) { padding-left: 14px; }
  .packages .col-1 { width: 364px; }
  .packages .col-2 { width: 387px; }
  .price-row {
    position: absolute; left: 25px; top: 451px; width: 1110px; display: flex;
    font-size: 15px; font-weight: 700; color: var(--text-body);
  }
  .price-row span { text-align: center; }
  .site-footer {
    position: absolute; left: 18px; top: 784px; width: 1170px; height: 84px;
    border-radius: 14px; border: 1px solid #7fa6e6;
    background: linear-gradient(180deg, #3c8cf0 0%, #1a6ae0 50%, #0e4fc8 100%);
  }
  .social { position: absolute; left: 26px; top: 26px; display: flex; gap: 5px; }
  .social span { width: 36px; height: 36px; border-radius: 4px; }
  .social .s1 { background: #3b5bb0; }
  .social .s2 { background: #4fb8e6; }
  .social .s3 { background: #ee6a1e; }
  .copyright {
    position: absolute; left: 0; right: 0; top: 35px; text-align: center;
    font-size: 13px; color: var(--text-white);
  }
  .footer-brand {
    position: absolute; right: 28px; top: 20px;
    display: flex; align-items: center; gap: 8px;
    font-size: 36px; font-weight: 700; color: var(--text-white);
  }
  .footer-brand .brand-mark { width: 24px; height: 24px; background: var(--text-white); }
</style>
</head>
<body>
  <header class="site-header">
    <div class="brand"><span class="brand-mark"></span>Vitalis</div>
    <div class="header-photo" role="img" aria-label="Bright modern lounge with large windows overlooking city towers"></div>
  </header>

  <svg class="phone-icon" width="124" height="124" viewBox="0 0 124 124" aria-hidden="true">
    <defs>
      <radialGradient id="phoneGlow" cx="40%" cy="30%" r="70%">
        <stop offset="0" stop-color="#6fa6f0"/>
        <stop offset="0.6" stop-color="#1f4fc0"/>
        <stop offset="1" stop-color="#0a2378"/>
      </radialGradient>
    </defs>
    <circle cx="62" cy="62" r="52" fill="url(#phoneGlow)" stroke="#c8d8f4" stroke-width="3"/>
    <path d="M30 50 Q62 30 94 50 L90 60 L78 56 L76 48 Q62 44 48 48 L46 56 L34 60 Z" fill="#ffffff"/>
    <path d="M44 62 L80 62 L88 86 L36 86 Z" fill="#ffffff"/>
    <circle cx="62" cy="74" r="7" fill="#1f4fc0"/>
  </svg>
  <div class="phone-number">555-010-200</div>

  <nav class="main-nav">
    <div class="nav-tab">About Us</div>
    <div class="nav-tab">VIP Club</div>
    <div class="nav-tab is-active">Services</div>
    <div class="nav-tab">Packages &amp; Prices</div>
    <div class="nav-tab is-register">Registration</div>
    <div class="nav-tab">Contacts</div>
  </nav>

  <main class="content-panel">
    <h1 class="panel-title">Services</h1>
    <table class="packages">
      <thead>
        <tr><th class="col-1">Package 1</th><th class="col-2">Package 2</th><th>Package 3</th></tr>
      </thead>
      <tbody>
        <tr><td>-Lorem ipsum</td><td>-Lorem ipsum</td><td>-Lorem ipsum</td></tr>
        <tr><td>-Lorem ipsum</td><td>-Lorem ipsum</td><td>-Lorem ipsum</td></tr>
        <tr><td>-Lorem ipsum</td><td>-Lorem ipsum</td><td>-Lorem ipsum</td></tr>
        <tr><td>-Lorem ipsum</td><td>-Lorem ipsum</td><td>-Lorem ipsum</td></tr>
        <tr><td>-Lorem ipsum</td><td>-Lorem ipsum</td><td>-Lorem ipsum</td></tr>
        <tr><td>-Lorem ipsum</td><td>-Lorem ipsum</td><td>-Lorem ipsum</td></tr>
        <tr><td>-Lorem ipsum</td><td>-Lorem ipsum</td><td>-Lorem ipsum</td></tr>
        <tr><td>-Lorem ipsum</td><td>-Lorem ipsum</td><td>-Lorem ipsum</td></tr>
        <tr><td>-Lorem ipsum</td><td>-Lorem ipsum</td><td>-Lorem ipsum</td></tr>
      </tbody>
    </table>
    <div class="price-row">
      <span style="width:364px">$000</span>
      <span style="width:387px">$000</span>
      <span style="width:359px">$000</span>
    </div>
  </main>

  <footer class="site-footer">
    <div class="social"><span class="s1"></span><span class="s2"></span><span class="s3"></span></div>
    <p class="copyright">Copyright ©2010 Vitalis. All Rights Reserved</p>
    <div class="footer-brand"><span class="brand-mark"></span>Vitalis</div>
  </footer>
</body>
</html>
```